I need a business card design for a new company that will be doing consulting work around issues of cultural competency, and diversity and inclusion. I would like the design to be crisp and clear with bold but conservative colors and incorporate shades of blue

Target Market(s)

Small businesses, schools, non-profits

Industry/Entity Type

Consulting

Font styles to use
Serif
Sans Serif

Colors
0c5ba6
6b449b
3276b5
0292cd

Requirements
Must have
• A Morrow Venture (name of company)
• Lemlem Tavish
• CEO
• lemlem@amorrowventure.com
• (215)483-2756

```html
<!DOCTYPE html>
<html lang="en">
<head>
<meta charset="utf-8">
<title>A Morrow Venture — Business Card</title>
<link rel="stylesheet" href="https://fonts.googleapis.com/css2?family=Jost:wght@400;500;700&display=swap">
<style>
  :root {
    --purple: #6b449b;
    --blue-deep: #0c5ba6;
    --blue-mid: #3276b5;
    --blue-bright: #0292cd;
    --paper: #ffffff;
  }
  * { margin: 0; padding: 0; box-sizing: border-box; }
  html, body { width: 1200px; height: 857px; overflow: hidden; background: var(--paper); }
  .card {
    position: relative;
    width: 1200px;
    height: 857px;
    background: var(--paper);
    font-family: "Jost", "Futura", sans-serif;
    color: var(--purple);
  }
  .contact__line {
    position: absolute;
    right: 43px;
    text-align: right;
    white-space: nowrap;
    line-height: 1;
  }
  .contact__name  { top: 44px;  font-weight: 700; font-size: 44px; letter-spacing: 0.5px; }
  .contact__title { top: 94px;  font-weight: 700; font-size: 22px; }
  .contact__email { top: 132px; font-weight: 400; font-size: 36px; letter-spacing: 0.5px; }
  .contact__phone { top: 187px; font-weight: 400; font-size: 36px; letter-spacing: 0.5px; }

  .company-name {
    position: absolute;
    left: 0;
    right: 0;
    top: 360px;
    text-align: center;
    font-weight: 500;
    font-size: 96px;
    line-height: 120px;
    color: var(--purple);
    white-space: nowrap;
  }

  .focus-list {
    position: absolute;
    left: 0;
    right: 0;
    top: 602px;
    list-style: none;
    display: flex;
    flex-direction: column;
    align-items: center;
    gap: 24px;
  }
  .focus-list__item {
    font-weight: 500;
    font-size: 40px;
    line-height: 52px;
    color: var(--blue-bright);
    white-space: nowrap;
  }
</style>
</head>
<body>
  <div class="card">
    <p class="contact__line contact__name">Lemlem Tavish</p>
    <p class="contact__line contact__title">CEO</p>
    <p class="contact__line contact__email">lemlem@amorrowventure.com</p>
    <p class="contact__line contact__phone">215-483-2756</p>

    <p class="company-name">A Morrow Venture</p>

    <ul class="focus-list">
      <li class="focus-list__item">Diversity</li>
      <li class="focus-list__item">Inclusion</li>
      <li class="focus-list__item">Cultural Competency</li>
    </ul>
  </div>
</body>
</html>
```